Home care support

Design a a great and dynamic website for a healthcare business. Our business will be involved in providing care at home for people with disability and the elderly. Below is a link that I found for a company offering similar services in the US. I am looking for something like this .
I have my files - the latest project in here in through through Pixelmarket
Sample site : https://cedarbrookassistedliving.com/
Target Market(s)
people with disability and elderly seniors who need home care support
Industry/Entity Type
Health
Coding
Coded - Design and coding required
Number of Pages Required
5+ page
Requirements
Must have
- inspirational pictures and designed with the themed logo (files attached)
Nice to have
- This is my sample and should look like this : https://cedarbrookassistedliving.com/

```html
<!DOCTYPE html>
<html lang="en">
<head>
<meta charset="utf-8">
<title>Maplecrest Healthcare — Home Care</title>
<link href="https://fonts.googleapis.com/css2?family=Montserrat:wght@400;500;600;700&family=Nunito+Sans:wght@400;600;800&family=Open+Sans:wght@400;600;700&display=swap" rel="stylesheet">
<style>
:root{
  --blue:#0b9ed9;
  --blue-deep:#1c64a8;
  --blue-dark:#0c5f9e;
  --green:#72b43c;
  --green-dark:#5f9e2e;
  --ink:#333d47;
  --muted:#6b7680;
  --pale:#eef6fb;
  --card:#eaf3f9;
  --white:#ffffff;
}
*{margin:0;padding:0;box-sizing:border-box}
html,body{width:1200px;height:4626px;overflow:hidden}
body{font-family:"Open Sans",sans-serif;color:var(--ink);background:var(--white);position:relative}
section,header,footer{position:absolute;left:0;width:1200px}
.abs{position:absolute}
.btn{position:absolute;display:flex;align-items:center;justify-content:center;color:#fff;font:700 12px "Montserrat",sans-serif;letter-spacing:.3px;border-radius:24px;text-transform:uppercase}
.btn-blue{background:var(--blue)}
.btn-green{background:var(--green)}
.title{font:400 38px "Montserrat",sans-serif;letter-spacing:.5px}
.title b{font-weight:700}
.t-green{color:var(--green)}
.t-blue{color:var(--blue-deep)}
.rule{position:absolute;height:3px;width:56px;background:var(--blue)}

/* header */
.site-header{top:0;height:100px;background:#fff;z-index:3;box-shadow:0 2px 6px rgba(0,0,0,.04)}
.nav{position:absolute;top:42px;font:500 13px "Montserrat",sans-serif;color:#55606a;text-transform:uppercase}
.nav.active{color:var(--blue-deep);border-bottom:2px solid var(--blue);padding-bottom:6px}
.brand-cap{position:absolute;left:470px;top:0;width:260px;height:135px;background:#fff;border-radius:0 0 130px 130px}
.brand{position:absolute;left:0;width:260px;text-align:center;font:700 30px "Montserrat",sans-serif;color:var(--blue-deep);letter-spacing:1px}
.brand-dot{position:absolute;left:105px;top:8px;width:50px;height:50px;border-radius:50%;background:var(--green)}
.brand-sub{position:absolute;left:0;top:105px;width:260px;text-align:center;font:500 9px "Montserrat",sans-serif;letter-spacing:6px;color:var(--blue)}
.phone-top{position:absolute;left:986px;top:34px;display:flex;align-items:center;gap:6px;font:600 14px "Montserrat",sans-serif;color:var(--blue)}
.icon-round{width:28px;height:28px;border-radius:50%;background:var(--blue);display:flex;align-items:center;justify-content:center}

/* hero */
.hero{top:100px;height:610px;background:linear-gradient(90deg,#f2f4f6 0%,#f7f8f9 45%,#eceff2 100%)}
.hero-bg{position:absolute;left:24px;top:0;width:1176px;height:610px;background:linear-gradient(120deg,#e9edf1,#f6f7f8 50%,#e4e8ec)}
.hero h2{position:absolute;left:115px;top:170px;font:400 38px "Nunito Sans",sans-serif;color:var(--blue-deep)}
.hero h1{position:absolute;left:115px;top:213px;font:800 52px "Nunito Sans",sans-serif;color:var(--blue-deep)}
.hero .tag{position:absolute;left:115px;top:288px;font:400 21px "Nunito Sans",sans-serif;color:var(--blue-deep)}
.hero-photo{position:absolute;left:628px;top:42px;width:470px;height:470px;border-radius:50%;background:linear-gradient(150deg,#d9cfc6,#efe7df 50%,#c8b7a9);border:12px solid var(--blue);box-shadow:-10px 8px 0 #7fcdee}

/* about */
.about{top:710px;height:547px}
.about-mark{position:absolute;left:126px;top:84px;width:416px;height:416px;border-radius:50%;background:linear-gradient(135deg,var(--blue) 0%,#6fc3e8 50%,var(--green) 100%)}
.about .title{position:absolute;left:611px;top:104px}
.about .rule{left:611px;top:152px;width:56px;height:3px;background:linear-gradient(90deg,var(--green),#b26a4c)}
.about p{position:absolute;left:609px;width:470px;font-size:15.5px;line-height:25px;color:#4d5660}

/* why */
.why{top:1257px;height:620px;overflow:hidden}
.why-photo{position:absolute;left:560px;top:0;width:640px;height:620px;background:linear-gradient(120deg,#cfe0ea,#e9dcd8 55%,#b9c9b0)}
.why .title{position:absolute;left:126px;top:122px;color:#fff}
.why .lead{position:absolute;left:126px;top:196px;width:440px;font-size:14.5px;line-height:24px;color:#fff}
.feature{position:absolute;width:230px;color:#fff}
.feature h4{position:absolute;left:50px;top:0;font:700 13.5px "Open Sans",sans-serif}
.feature p{position:absolute;left:50px;top:20px;width:180px;font-size:11px;line-height:16px;color:#e2f3fb}
.feature svg{position:absolute;left:0;top:0}

/* services */
.services{top:1877px;height:512px}
.services .title{position:absolute;left:0;width:1200px;text-align:center;top:88px}
.services .rule{left:572px;top:140px}
.svc{position:absolute;top:185px;width:183px;height:228px;background:var(--card);border-radius:52px 0 0 52px;text-align:center}
.svc.active{background:var(--green)}
.svc svg{position:absolute;left:70px;top:44px}
.svc h4{position:absolute;left:0;width:183px;top:106px;font:700 13.5px "Open Sans",sans-serif;color:var(--blue-deep);line-height:17px}
.svc p{position:absolute;left:20px;width:143px;top:142px;font-size:9.5px;line-height:15px;color:#8a949d}
.svc.active h4,.svc.active p{color:#fff}
.svc.active svg *{stroke:#fff}

/* approach */
.approach{top:2389px;height:601px;background:var(--pale);overflow:hidden}
.approach-photo{position:absolute;left:575px;top:10px;width:820px;height:820px;border-radius:50%;background:linear-gradient(135deg,#ede6de,#d8cfc4 50%,#9aa6b6);border-left:8px solid var(--blue)}
.approach h3{position:absolute;left:129px;font:400 26px "Montserrat",sans-serif}
.approach .rule{left:129px;top:243px;width:56px}
.approach p{position:absolute;left:129px;top:270px;width:420px;font-size:14px;line-height:24px;color:#4d5660}

/* blogs */
.blogs{top:2990px;height:670px}
.blogs .title{position:absolute;left:0;width:1200px;text-align:center;top:80px}
.blogs .rule{left:572px;top:132px}
.post{position:absolute;top:167px;width:307px;height:413px;border:1px solid #d6e6f1;background:#fff}
.post-img{height:207px;background:linear-gradient(135deg,#dfe6ea,#c9d3d9 50%,#aebac4)}
.post-date{position:absolute;left:28px;top:228px;font:700 12.5px "Open Sans",sans-serif;color:var(--blue);display:flex;gap:6px;align-items:center}
.post h4{position:absolute;left:28px;top:252px;width:260px;font:700 14px "Open Sans",sans-serif;line-height:20px;color:var(--blue-deep)}
.post p{position:absolute;left:28px;top:302px;width:260px;font-size:12.5px;line-height:19px;color:#6b7680}

/* contact */
.contact{top:3660px;height:593px;background:linear-gradient(120deg,#1785cc,#0e9ad8 60%,#1b8fd2);overflow:hidden}
.contact .title{position:absolute;left:149px;top:125px;color:#fff}
.contact .lead{position:absolute;left:146px;top:190px;width:420px;font-size:13px;line-height:22px;color:#e6f4fb}
.c-item{position:absolute;left:140px;color:#fff}
.c-item .ring{position:absolute;left:0;top:0;width:64px;height:64px;border-radius:50%;border:2px solid #fff;display:flex;align-items:center;justify-content:center}
.c-item h5{position:absolute;left:76px;top:10px;font:700 13px "Open Sans",sans-serif;white-space:nowrap}
.c-item span{position:absolute;left:76px;top:30px;font-size:20px;white-space:nowrap}
.form-card{position:absolute;left:584px;top:94px;width:498px;height:404px;background:#fff;border-radius:70px 0 0 70px}
.field{position:absolute;left:54px;width:389px;height:42px;border:1.5px solid #c9d5de;font-size:12px;color:#7d8790;padding:12px 16px}
</style>
</head>
<body>

<header class="site-header">
  <a class="nav active" style="left:110px">About Us</a>
  <a class="nav" style="left:228px">Services</a>
  <a class="nav" style="left:358px">Resource</a>
  <div class="brand-cap">
    <div class="brand-dot"></div>
    <div class="brand" style="top:66px">MAPLECREST</div>
    <div class="brand-sub">HEALTHCARE</div>
  </div>
  <a class="nav" style="left:731px">Blogs</a>
  <a class="nav" style="left:816px">FAQ</a>
  <a class="nav" style="left:880px">Contact Us</a>
  <div class="phone-top">
    <span class="icon-round"><svg width="14" height="14" viewBox="0 0 24 24"><path d="M6.6 10.8a15 15 0 0 0 6.6 6.6l2.2-2.2c.3-.3.7-.4 1-.2 1.1.4 2.3.6 3.6.6.6 0 1 .4 1 1V20c0 .6-.4 1-1 1A17 17 0 0 1 3 4c0-.6.4-1 1-1h3.5c.6 0 1 .4 1 1 0 1.3.2 2.5.6 3.6.1.3 0 .7-.2 1z" fill="#fff"/></svg></span>
    (555) 214 8830
  </div>
</header>

<section class="hero">
  <div class="hero-bg" role="img" aria-label="Soft, blurred bright living room behind the headline"></div>
  <h2>We are Committed to</h2>
  <h1>Provide Best Care</h1>
  <div class="tag">The Best Care is Home Care.</div>
  <a class="btn btn-blue" style="left:110px;top:338px;width:212px;height:46px">Book Appointment</a>
  <a class="btn btn-green" style="left:330px;top:338px;width:212px;height:46px">Call (555) 214 8830</a>
  <div class="hero-photo" role="img" aria-label="Photo of a smiling elderly woman with a young caregiver embracing her"></div>
</section>

<section class="about">
  <div class="about-mark" role="img" aria-label="Brand emblem area in blue and green"></div>
  <h2 class="title"><span class="t-green">ABOUT</span> <b class="t-blue">MAPLECREST</b></h2>
  <div class="rule"></div>
  <p style="top:180px">Lorem ipsum dolor sit amet, consectetur adipiscing elit, sed do eiusmod tempor incididunt ut labore</p>
  <p style="top:262px">voluptatem. Ut enim ad minima veniam, quis nostrum exercitationem ullam corporis suscipit laboriosam, nisi ut aliquid ex ea commodi consequatur? Quis autem vel eum iure reprehenderit qui in ea voluptate velit esse quam nihil molestiae consequatur, vel illum qui dolorem</p>
  <a class="btn btn-blue" style="left:611px;top:409px;width:167px;height:48px">Learn More</a>
</section>

<section class="why">
  <div class="why-photo" role="img" aria-label="Photo of a nurse in blue scrubs holding hands with a smiling elderly woman"></div>
  <svg class="abs" style="left:0;top:0" width="1200" height="620" viewBox="0 0 1200 620">
    <defs>
      <linearGradient id="whyFill" x1="0" y1="0" x2="1" y2="0">
        <stop offset="0" stop-color="#0b98d6"/>
        <stop offset=".42" stop-color="#0da0da"/>
        <stop offset=".62" stop-color="#0da0da" stop-opacity=".35"/>
        <stop offset=".8" stop-color="#0da0da" stop-opacity="0"/>
      </linearGradient>
    </defs>
    <path d="M0 5 C300 -15 700 -5 1200 80 L1200 0 L0 0Z" fill="#fff"/>
    <path d="M600 5 C850 15 1050 40 1200 80 L1200 60 C1050 25 850 5 600 5Z" fill="#72b43c"/>
    <path d="M0 5 C300 -15 700 -5 1200 80 L1200 620 L0 620Z" fill="url(#whyFill)"/>
    <path d="M0 520 C200 580 500 610 1200 600 L1200 620 L0 620Z" fill="#fff"/>
    <path d="M0 520 C200 580 500 610 900 606 C500 600 200 565 0 500Z" fill="#72b43c"/>
  </svg>
  <h2 class="title"><span>WHY CHOOSE</span> <b>MAPLECREST</b></h2>
  <p class="lead">Lorem ipsum dolor sit amet, consectetur adipiscing elit, sed do eiusmod tempor incididunt ut labore</p>
  <div class="feature" style="left:126px;top:276px">
    <svg width="40" height="50" viewBox="0 0 40 50" fill="none" stroke="#fff" stroke-width="2"><circle cx="20" cy="14" r="8"/><path d="M12 8h16M4 48c0-12 7-18 16-18s16 6 16 18Z"/></svg>
    <h4>Friendly Staff</h4><p>Lorem ipsum dolor sit amet, consectetur adipiscin</p>
  </div>
  <div class="feature" style="left:370px;top:276px">
    <svg width="44" height="44" viewBox="0 0 44 44" fill="none" stroke="#fff" stroke-width="2"><path d="M22 16c-3-6-12-5-12 2 0 5 12 12 12 12s12-7 12-12c0-7-9-8-12-2Z"/><path d="M4 14v14l10 12M40 14v14l-10 12"/></svg>
    <h4>Choice of Caregiver</h4><p>Lorem ipsum dolor sit amet, consectetur adipiscin</p>
  </div>
  <div class="feature" style="left:126px;top:383px">
    <svg width="44" height="48" viewBox="0 0 44 48" fill="none" stroke="#fff" stroke-width="2"><path d="M6 28v-6a16 16 0 0 1 32 0v6"/><rect x="3" y="26" width="8" height="14" rx="3"/><rect x="33" y="26" width="8" height="14" rx="3"/><path d="M37 40c0 5-6 6-12 6"/></svg>
    <h4>On Call 24/7</h4><p>Lorem ipsum dolor sit amet, consectetur adipiscin</p>
  </div>
  <div class="feature" style="left:370px;top:383px">
    <svg width="40" height="44" viewBox="0 0 40 44" fill="none" stroke="#fff" stroke-width="2"><path d="M10 42V32C4 28 3 20 6 13 10 4 22 2 30 8c6 5 6 12 5 16l3 5h-4v6h-6v7"/><circle cx="20" cy="18" r="6"/></svg>
    <h4>Peace of Mind</h4><p>Lorem ipsum dolor sit amet, consectetur adipiscin</p>
  </div>
</section>

<section class="services">
  <h2 class="title"><span class="t-green">OUR</span> <b class="t-blue">SERVICES</b></h2>
  <div class="rule"></div>
  <div class="svc active" style="left:138px">
    <svg width="44" height="44" viewBox="0 0 44 44" fill="none" stroke-width="2"><path d="M4 22 22 6l18 16M9 18v22h26V18" stroke="#fff"/><rect x="16" y="24" width="12" height="10" stroke="#fff"/><path d="M22 24v10M16 29h12" stroke="#fff"/></svg>
    <h4>Light<br>Housekeeping</h4>
    <p style="top:146px">Sed ut persp iciatis unde omnis iste natus error sit</p>
  </div>
  <div class="svc" style="left:336px">
    <svg width="44" height="44" viewBox="0 0 44 44" fill="none" stroke="#1c64a8" stroke-width="2"><rect x="6" y="4" width="32" height="36" rx="3"/><path d="M6 12h32"/><circle cx="22" cy="26" r="9"/><circle cx="24" cy="28" r="4" stroke="#0b9ed9"/></svg>
    <h4>Laundry &amp; Linens</h4>
    <p>Sed ut persp iciatis unde omnis iste natus error sit Sed ut persp iciatis unde omnis iste</p>
  </div>
  <div class="svc" style="left:537px">
    <svg width="44" height="44" viewBox="0 0 44 44" fill="none" stroke="#1c64a8" stroke-width="2"><rect x="8" y="4" width="20" height="8" rx="2"/><rect x="6" y="12" width="24" height="28" rx="3"/><path d="M18 20v12M12 26h12" stroke="#0b9ed9"/><rect x="28" y="26" width="12" height="8" rx="4"/></svg>
    <h4>Medication Care</h4>
    <p>Sed ut persp iciatis unde omnis iste natus error sit Sed ut persp iciatis unde omnis iste</p>
  </div>
  <div class="svc" style="left:736px">
    <svg width="44" height="44" viewBox="0 0 44 44" fill="none" stroke="#1c64a8" stroke-width="2"><circle cx="22" cy="22" r="18"/><circle cx="22" cy="22" r="12" stroke="#0b9ed9"/><path d="M16 16l12 12M28 16 16 28"/></svg>
    <h4>Meal Preparation</h4>
    <p>Sed ut persp iciatis unde omnis iste natus error sit Sed ut persp iciatis unde omnis iste</p>
  </div>
  <div class="svc" style="left:929px">
    <svg width="44" height="44" viewBox="0 0 44 44" fill="none" stroke="#1c64a8" stroke-width="2" style="top:34px"><path d="M4 24h36v6a8 8 0 0 1-8 8H12a8 8 0 0 1-8-8Z"/><path d="M10 38l-2 4M34 38l2 4M30 24V8a4 4 0 0 1 8 0v2"/><circle cx="20" cy="14" r="3" stroke="#0b9ed9"/></svg>
    <h4 style="top:100px">Kitchen &amp;<br>Bathroom Care</h4>
    <p style="top:142px">Sed ut persp iciatis unde omnis iste natus error sit Sed ut persp iciatis unde omnis iste</p>
  </div>
</section>

<section class="approach">
  <div class="approach-photo" role="img" aria-label="Photo of a caregiver helping an elderly woman up from a wheelchair"></div>
  <h3 class="t-green" style="top:160px">SIMPLE, AFFORDABLE</h3>
  <h3 class="t-blue" style="top:196px;font-weight:600">APPROACH TO HOME CARE</h3>
  <div class="rule"></div>
  <p>Lorem ipsum dolor sit amet, consectetur adipiscing elit, sed do eiusmod tempor incididunt ut labore et dolore magna aliqua. Ut enim ad minim veniam, quis nostru.Lorem ipsum dolor sit amet, consectetur adipiscing elit, sed do eiusmod tempor incididunt ut labore et dolore magna aliqua.</p>
  <a class="btn btn-blue" style="left:123px;top:410px;width:168px;height:48px">Learn More</a>
</section>

<section class="blogs">
  <h2 class="title"><span class="t-green">LATEST</span> <b class="t-blue">BLOGS</b></h2>
  <div class="rule"></div>
  <article class="post" style="left:138px">
    <div class="post-img" role="img" aria-label="Photo of a carer exercising with a man in a wheelchair"></div>
    <div class="post-date"><svg width="13" height="13" viewBox="0 0 14 14"><rect x="1" y="2" width="12" height="11" rx="1" fill="none" stroke="#0b9ed9" stroke-width="1.6"/><path d="M1 6h12M4 0v3M10 0v3" stroke="#0b9ed9" stroke-width="1.6"/></svg>25 MAR 2022</div>
    <h4>Lorem ipsum dolor sit amet, cons ectetur adipiscing elit</h4>
    <p>Sed ut perspiciatis unde omnis iste natus error sit voluptatem accusantium</p>
    <a class="btn btn-green" style="left:26px;top:354px;width:132px;height:36px;font-size:11px">Learn More</a>
  </article>
  <article class="post" style="left:462px">
    <div class="post-img" role="img" aria-label="Photo of a nurse talking with an elderly man holding a cane"></div>
    <div class="post-date"><svg width="13" height="13" viewBox="0 0 14 14"><rect x="1" y="2" width="12" height="11" rx="1" fill="none" stroke="#0b9ed9" stroke-width="1.6"/><path d="M1 6h12M4 0v3M10 0v3" stroke="#0b9ed9" stroke-width="1.6"/></svg>25 MAR 2022</div>
    <h4>Lorem ipsum dolor sit amet, cons ectetur adipiscing elit</h4>
    <p>Sed ut perspiciatis unde omnis iste natus error sit voluptatem accusantium</p>
    <a class="btn btn-green" style="left:26px;top:354px;width:132px;height:36px;font-size:11px">Learn More</a>
  </article>
  <article class="post" style="left:785px">
    <div class="post-img" role="img" aria-label="Photo of a carer serving a meal to an elderly woman at a table"></div>
    <div class="post-date"><svg width="13" height="13" viewBox="0 0 14 14"><rect x="1" y="2" width="12" height="11" rx="1" fill="none" stroke="#0b9ed9" stroke-width="1.6"/><path d="M1 6h12M4 0v3M10 0v3" stroke="#0b9ed9" stroke-width="1.6"/></svg>25 MAR 2022</div>
    <h4>Lorem ipsum dolor sit amet, cons ectetur adipiscing elit</h4>
    <p>Sed ut perspiciatis unde omnis iste natus error sit voluptatem accusantium</p>
    <a class="btn btn-green" style="left:26px;top:354px;width:132px;height:36px;font-size:11px">Learn More</a>
  </article>
</section>

<section class="contact" role="region" aria-label="Contact section over a blue-tinted photo of a caregiver and senior">
  <h2 class="title"><span>CONTACT</span> <b>US</b></h2>
  <p class="lead">Morbi diam mauris viverra in gravida eu mattis in anquam Curabitur vel dolor ultrices ipsum dictum tristique</p>
  <div class="c-item" style="top:268px">
    <div class="ring"><svg width="30" height="22" viewBox="0 0 30 22" fill="none" stroke="#fff" stroke-width="1.8"><rect x="5" y="1" width="24" height="20"/><path d="M5 1l12 11L29 1M0 8h4M0 12h4M0 16h4"/></svg></div>
    <h5>E-mail address</h5><span>care@maplecresthome.com</span>
  </div>
  <div class="c-item" style="top:346px">
    <div class="ring"><svg width="28" height="28" viewBox="0 0 24 24" fill="none" stroke="#fff" stroke-width="1.5"><path d="M6.6 10.8a15 15 0 0 0 6.6 6.6l2.2-2.2c.3-.3.7-.4 1-.2 1.1.4 2.3.6 3.6.6.6 0 1 .4 1 1V20c0 .6-.4 1-1 1A17 17 0 0 1 3 4c0-.6.4-1 1-1h3.5c.6 0 1 .4 1 1 0 1.3.2 2.5.6 3.6.1.3 0 .7-.2 1z"/></svg></div>
    <h5>Phone Number</h5><span>(555) 214 8831</span>
  </div>
  <div class="form-card">
    <div class="field" style="top:52px">Name</div>
    <div class="field" style="top:104px">E-mail address</div>
    <div class="field" style="top:158px">Phone Number</div>
    <div class="field" style="top:212px;height:98px">Message</div>
    <a class="btn btn-green" style="left:56px;top:326px;width:132px;height:36px;font-size:11px">Learn More</a>
  </div>
</section>

<footer style="top:4253px;height:373px">
  <div class="abs" style="left:172px;top:62px;width:90px;height:90px;border-radius:50%;background:var(--green)"></div>
  <div class="abs" style="left:110px;top:160px;font:700 30px 'Montserrat',sans-serif;color:var(--blue-deep)">MAPLECREST</div>
  <div class="abs" style="left:126px;top:198px;font:500 9px 'Montserrat',sans-serif;letter-spacing:7px;color:var(--blue)">HEALTHCARE</div>

  <div class="abs" style="left:411px;top:76px">
    <h4 style="font:600 15px 'Montserrat',sans-serif;color:var(--blue-deep);border-bottom:2px solid var(--blue);padding-bottom:2px">NAVIGATION</h4>
    <p style="margin-top:20px;font-size:12.5px;line-height:25px;color:#5b6570">About Us<br>Our Services<br>Blogs<br>Book appointment</p>
  </div>
  <div class="abs" style="left:623px;top:76px">
    <h4 style="font:600 15px 'Montserrat',sans-serif;color:var(--blue-deep);border-bottom:2px solid var(--blue);padding-bottom:2px">RESOURCES</h4>
    <p style="margin-top:20px;font-size:12.5px;line-height:25px;color:#5b6570">Privacy Policy<br>Testimonials<br>FAQ<br>Contact Us</p>
  </div>
  <div class="abs" style="left:815px;top:76px;width:260px">
    <h4 style="font:600 15px 'Montserrat',sans-serif;color:var(--blue-deep);border-bottom:2px solid var(--blue);padding-bottom:2px;display:inline-block">CONTACT US</h4>
    <div style="margin-top:18px;display:flex;align-items:center;gap:8px;font:600 12.5px 'Open Sans',sans-serif;color:#4d5660"><span class="icon-round" style="width:24px;height:24px"><svg width="12" height="12" viewBox="0 0 24 24"><path d="M6.6 10.8a15 15 0 0 0 6.6 6.6l2.2-2.2c.3-.3.7-.4 1-.2 1.1.4 2.3.6 3.6.6.6 0 1 .4 1 1V20c0 .6-.4 1-1 1A17 17 0 0 1 3 4c0-.6.4-1 1-1h3.5c.6 0 1 .4 1 1 0 1.3.2 2.5.6 3.6.1.3 0 .7-.2 1z" fill="#fff"/></svg></span>Location: Boulder, CO</div>
    <div style="margin-top:10px;display:flex;align-items:center;gap:8px;font:600 12.5px 'Open Sans',sans-serif;color:#4d5660"><span class="icon-round" style="width:24px;height:24px"><svg width="12" height="14" viewBox="0 0 12 16"><path d="M6 0a6 6 0 0 1 6 6c0 4-6 10-6 10S0 10 0 6a6 6 0 0 1 6-6Z" fill="#fff"/><circle cx="6" cy="6" r="2.2" fill="#0b9ed9"/></svg></span>Phone: 303-555-0148</div>
    <p style="margin-top:18px;font-size:12.5px;color:#5b6570">Locally Owned, Nationally supported</p>
  </div>

  <div class="abs" style="left:0;top:309px;width:1200px;height:64px;background:#eef3f7;display:flex;align-items:center;justify-content:center;font-size:12px;color:#6b7680">© Copyright 2022 Maplecrest | All Right Reserved</div>
</footer>

</body>
</html>
```